Wellness Web Design Project

web design for business called Lumen Harbor Wellness. I have a private practice for which i need patients. I teach in house and online courses for professional and the public. It will be both an educational site as well as a marketing site and it will have a store and a member login area. I do sonic acupuncture called vibrelaxis. It is based on demarchetos' music of the spheres. I use vibrational and harmonic therapies to harmonize cells psyches and souls! it is the most scientifically rooted of the alternative therapies available and i focus on womens health, pediatric, emotional problems and spiritual awakening. I need it to be a balance of spiritual and symbolic depth as well as being graceful sophisticated grounded. I want it to look incredibly elegant, sophisticated, and established, not airy fairy! i like a minimal approach, fresh air, clean, confident, expensive, luxurious but also playful. im not trying to mold myself into the usual framework. i am trying to convey a sense of unleashing power and purpose and pleasure. i need it to be Gorgeous and relatable while being original
i have included the site map as an upload and here is a link to all the things that a home page should include. I have the logo and other versions that i will use to promote the different online programs i have. I may have a 'sound logo' start as the page comes up. the sounds are ethereal tones rather than music and super gentle and mysterious without being cloying or overly emotional. I work with the physical body, emotional trauma and altered states so many hats and have many different prongs to what i do so organization and clarity is important without getting cluttered. want to convert and capture into my email list for sure and have free downloadable content to provide.
the logo i have designed speaks volumes about my aesthetic. i have included a flyer made - which is 1. direction, but i am interested in seeing some designs that play with white space as well. the 'look' of the flyer has never been published and so am in no way married to it. I will include some of the photo i will want to use along the way that give you some sense of things or things to riff off. some of the photos of me have alot of solid blocks of color... i have included one of them. I am very sensitive to sophistication of color.
the site map i have included is jsut my attempt to organize - i am not married to it!
thankyou so much, and if you haven;t yet discovered the power of sound to alter brain waves and cell functioning wherever you are in the world - I highly recommend it:)

Target Market(s)

women 25-55's educated, familiar with alternative healing and conscious living who have money to spend on wellness

Industry/Entity Type

Business

Requirements
Must have
• http://notes.brimfaldo.com/notes/tabid/4821/bid/58204/12-Critical-Elements-Every-Homepage-Must-Have-Infographic.aspx
these are some of the elements that seem to be necessary
plus social media links....

```html
<!DOCTYPE html>
<html lang="en">
<head>
<meta charset="utf-8">
<title>Lumen Harbor Wellness</title>
<link rel="stylesheet" href="https://fonts.googleapis.com/css2?family=Comfortaa:wght@400&family=Poiret+One&family=Raleway:ital,wght@0,400;0,600;0,700;1,600&family=Open+Sans:wght@400;600&display=swap">
<style>
:root{
  --teal:#72c0c0;
  --teal-text:#5bb4b4;
  --brand-green:#2b8a3e;
  --ink:#1c1c1c;
  --body:#333;
  --rule:#dcdcdc;
  --paper:#fff;
  --gold:#e8b33a;
}
*{box-sizing:border-box;margin:0;padding:0}
html,body{width:826px;height:1200px;overflow:hidden;background:var(--paper)}
body{position:relative;font-family:'Raleway',sans-serif;color:var(--body)}
.abs{position:absolute}

/* header */
.brand-mark{left:52px;top:14px;width:46px;height:46px;border-radius:50%;border:3px solid var(--brand-green);background:var(--gold)}
.brand-name{left:113px;top:12px;font-family:'Comfortaa',sans-serif;font-size:30px;color:var(--brand-green);white-space:nowrap;letter-spacing:.3px}
.brand-tagline{left:113px;top:50px;font-family:'Comfortaa',sans-serif;font-size:15px;color:var(--brand-green);white-space:nowrap}
.field{left:604px;width:175px;height:22px;border:1px solid var(--rule);font-size:9px;color:var(--ink);padding:5px 0 0 10px}
.newsletter{top:18px}
.newsletter .go{position:absolute;right:2px;top:2px;width:17px;height:16px;border:1px solid #bbb;font-size:8px;text-align:center;line-height:14px}
.search{top:46px}
.search svg{position:absolute;right:6px;top:5px}

/* nav */
.main-nav{left:48px;top:88px;width:731px;height:37px;background:var(--teal)}
.nav-link{top:11px;font-size:11.5px;color:#fff;transform:translateX(-50%);white-space:nowrap}
.nav-sep{top:8px;width:1px;height:22px;background:rgba(255,255,255,.45)}
.social-dot{border-radius:50%;background:#fff}

/* hero */
.hero{left:48px;top:125px;width:731px;height:282px;background:linear-gradient(100deg,#f4f4f2 0%,#eef0ec 38%,#e8cdbb 55%,#d9ad92 66%,#6b5040 78%,#e9eee6 92%,#f3f5f2 100%)}
.hero-title{left:102px;top:166px;font-family:'Open Sans',sans-serif;font-size:26px;color:var(--ink)}
.hero-kicker{left:102px;top:211px;font-family:'Open Sans',sans-serif;font-size:12.5px;color:var(--brand-green)}
.hero-sub{left:102px;top:231px;font-family:'Open Sans',sans-serif;font-size:17px;font-weight:600;color:var(--ink)}
.btn{background:var(--teal);color:#fff;text-align:center}
.hero-btn{left:103px;top:269px;width:87px;height:19px;font-size:10px;line-height:19px;font-family:'Open Sans',sans-serif}
.dot{top:381px;width:6px;height:6px;border-radius:50%;background:var(--teal)}
.dot.active{background:transparent;border:1px solid var(--teal)}

/* panels */
.panel{border:1px solid var(--rule);background:#fff}
.why{left:48px;top:433px;width:494px;height:201px}
.watch{left:550px;top:433px;width:229px;height:201px}
.display{font-family:'Poiret One',sans-serif;white-space:nowrap}
.why-title{left:67px;top:448px;font-size:29px;color:var(--ink)}
.why-lead{left:68px;top:489px;width:460px;font-size:10.5px;font-weight:700;line-height:13.5px;color:var(--ink)}
.why-lead .accent{color:var(--teal-text)}
.why-body{left:69px;top:540px;width:456px;font-size:8.6px;line-height:13.5px;color:var(--ink)}
.keep-reading{left:451px;top:606px;width:77px;height:18px;font-size:8.5px;line-height:18px;font-weight:600}
.watch-title{left:567px;top:443px;font-size:26px;color:var(--teal-text)}
.watch-title b{font-weight:400;font-family:'Comfortaa',sans-serif;font-size:24px}
.watch-text{left:567px;top:483px;width:196px;font-size:8.8px;line-height:13.5px;color:var(--ink)}
.video{left:568px;top:538px;width:192px;height:78px;background:radial-gradient(ellipse at 45% 60%,#a6d94a 0%,#86c43a 45%,#5fa52f 100%)}
.expand{left:696px;top:605px;width:63px;height:11px;font-size:7px;line-height:11px}

.about{left:48px;top:661px;width:731px;height:181px}
.portrait{left:72px;top:683px;width:133px;height:133px;background:linear-gradient(135deg,#4a6b2f,#7aa04a 50%,#3e5a28)}
.about-title{left:237px;top:679px;font-size:26px;color:var(--teal-text)}
.about-quote{left:237px;top:713px;width:525px;font-size:8.7px;font-weight:600;font-style:italic;line-height:13.8px;color:var(--ink)}
.about-body{left:237px;top:764px;width:525px;font-size:8.7px;line-height:13.8px;color:var(--body)}

/* feature cards */
.card-img{top:868px;width:175px;height:133px;border:1px solid #eee}
.card-title{top:1016px;width:175px;text-align:center;font-size:11.5px;color:var(--teal-text);letter-spacing:.2px}
.card-text{top:1034px;width:175px;text-align:center;font-size:8.3px;line-height:12.5px;color:var(--ink)}
.card-btn{top:1070px;width:55px;height:14px;font-size:5.5px;line-height:14px;letter-spacing:.3px}

/* footer */
.footer-rule{left:48px;top:1112px;width:731px;height:1px;background:var(--rule)}
.footer-nav{left:69px;top:1136px;font-size:9.3px;color:var(--ink);white-space:nowrap;word-spacing:0}
.footer-nav span{margin-right:8px}
.footer-social{top:1134px;width:15px;height:15px;border-radius:50%;background:var(--ink)}
.copyright{left:560px;top:1168px;width:189px;text-align:right;font-family:'Open Sans',sans-serif;font-size:6.8px;color:var(--ink)}
</style>
</head>
<body>

<header>
  <div class="abs brand-mark" aria-hidden="true"></div>
  <div class="abs brand-name">Lumen Harbor Wellness</div>
  <div class="abs brand-tagline">Vibrelaxis - sonic acupuncture</div>
  <div class="abs field newsletter">Email - Join our newsletter<span class="go">Go</span></div>
  <div class="abs field search">Search
    <svg width="8" height="11" viewBox="0 0 8 11"><path d="M1 1l5 4.5L1 10" fill="none" stroke="#333" stroke-width="1.4"/></svg>
  </div>
</header>

<nav class="abs main-nav" aria-label="Main">
</nav>
<div class="abs nav-link" style="left:109px;top:99px">Home</div>
<div class="abs nav-sep" style="left:147px;top:96px"></div>
<div class="abs nav-link" style="left:193px;top:99px">Vibrelaxis</div>
<div class="abs nav-sep" style="left:241px;top:96px"></div>
<div class="abs nav-link" style="left:285px;top:99px">About Us</div>
<div class="abs nav-sep" style="left:330px;top:96px"></div>
<div class="abs nav-link" style="left:383px;top:99px">Our Services</div>
<div class="abs nav-sep" style="left:437px;top:96px"></div>
<div class="abs nav-link" style="left:492px;top:99px">Wellness Tips</div>
<div class="abs nav-sep" style="left:547px;top:96px"></div>
<div class="abs nav-link" style="left:597px;top:99px">Contact Us</div>
<div class="abs social-dot" style="left:684px;top:99px;width:14px;height:14px" role="img" aria-label="Social network link"></div>
<div class="abs social-dot" style="left:718px;top:99px;width:14px;height:14px" role="img" aria-label="Social network link"></div>
<div class="abs social-dot" style="left:750px;top:99px;width:14px;height:14px" role="img" aria-label="Social network link"></div>

<section>
  <div class="abs hero" role="img" aria-label="Woman relaxing on a treatment table while a practitioner holds her head"></div>
  <h1 class="abs hero-title" style="font-weight:400">Harmonic Sound Healing</h1>
  <p class="abs hero-kicker">Lorem ipsum dolor sit amet, consectetur adipiscing elit</p>
  <p class="abs hero-sub">Lorem ipsum dolor sit amet, consectetur</p>
  <div class="abs btn hero-btn">Learn More</div>
  <svg class="abs" style="left:57px;top:239px" width="22" height="38" viewBox="0 0 22 38"><path d="M20 1L2 19l18 18" fill="none" stroke="#222" stroke-width="1.8"/></svg>
  <svg class="abs" style="left:748px;top:239px" width="22" height="38" viewBox="0 0 22 38"><path d="M2 1l18 18L2 37" fill="none" stroke="#222" stroke-width="1.8"/></svg>
  <div class="abs dot active" style="left:100px"></div>
  <div class="abs dot" style="left:114px"></div>
  <div class="abs dot" style="left:128px"></div>
  <div class="abs dot" style="left:142px"></div>
</section>

<section>
  <div class="abs panel why"></div>
  <h2 class="abs display why-title" style="font-weight:400">Why Vibrelaxis</h2>
  <p class="abs why-lead">Lorem Ipsum <span class="accent">Dolor sit amet,</span> consectetur adipiscing elit. Sed at ante. Mauris eleifend, quam a vulputate dictum, massa quam dapibus leo, <span class="accent">eget vulputate</span> orci purus ut lorem.</p>
  <p class="abs why-body"><b>Lorem ipsum dolor sit amet,</b> consectetur adipiscing elit. Sed at ante. Mauris eleifend, quam a vulputate dictum, massa quam dapibus leo, eget vulputate orci purus ut lorem. In fringilla mi in ligula. Pellentesque aliquam quam vel dolor. <b><i>Nunc adipiscing.</i></b> Sed quam odio, tempus ac, aliquam molestie, varius ac, tellus. Lorem ipsum dolor sit amet, consectetur adipiscing elit. Sed at ante. Mauris eleifend, quam a vulputate dictum, massa quam dapibus leo, eget vulputate orci purus ut lorem...</p>
  <div class="abs btn keep-reading">Keep Reading</div>

  <div class="abs panel watch"></div>
  <h2 class="abs display watch-title" style="font-weight:400">Watch <b>Vibrelaxis</b></h2>
  <p class="abs watch-text">Lorem ipsum dolor sit amet, consectetur adipiscing elit. Sed at ante. <b>Mauris eleifend,</b> quam a vulputate dictum.</p>
  <div class="abs video" role="img" aria-label="Video still of a green seedling sprouting"></div>
  <div class="abs btn expand">Expand Video</div>
</section>

<section>
  <div class="abs panel about"></div>
  <div class="abs portrait" role="img" aria-label="Portrait of Dr Maren Vellacott outdoors"></div>
  <h2 class="abs display about-title" style="font-weight:400">About Dr Maren Vellacott</h2>
  <p class="abs about-quote">"Lorem ipsum dolor sit amet, consectetur adipiscing elit. Sed at ante. Mauris eleifend, quam a vulputate dictum, massa quam dapibus leo, eget vulputate orci purus ut lorem. In fringilla mi in ligula. Pellentesque aliquam quam vel dolor. Nunc adipiscing. Sed quam odio, tempus ac, aliquam molestie, varius ac, tellus"</p>
  <p class="abs about-body">Lorem ipsum dolor sit amet, consectetur adipiscing elit. Sed at ante. Mauris eleifend, quam a vulputate dictum, massa quam dapibus leo, eget vulputate orci purus ut lorem. In fringilla mi in ligula. Pellentesque aliquam quam vel dolor. Nunc adipiscing. Sed quam odio, tempus ac, aliquam molestie, varius ac, tellus.</p>
</section>

<section>
  <div class="abs card-img" style="left:48px;background:linear-gradient(135deg,#f6f4f2,#e9cdb9 55%,#f3efec)" role="img" aria-label="Woman receiving acupuncture on her back"></div>
  <div class="abs card-title" style="left:48px">LOREM IPSUM DOLOR SIT</div>
  <p class="abs card-text" style="left:48px">Lorem ipsum dolor sit amet, consectetur adipiscing elit. Sed at ante.</p>
  <div class="abs btn card-btn" style="left:112px">READ MORE</div>

  <div class="abs card-img" style="left:233px;background:linear-gradient(120deg,#2e4a22,#5c7a3a 45%,#d8c8b8 70%,#efe7df)" role="img" aria-label="Hands resting in a meditation pose outdoors"></div>
  <div class="abs card-title" style="left:233px">LOREM IPSUM DOLOR SIT</div>
  <p class="abs card-text" style="left:233px">Lorem ipsum dolor sit amet, consectetur adipiscing elit. Sed at ante.</p>
  <div class="abs btn card-btn" style="left:298px">READ MORE</div>

  <div class="abs card-img" style="left:419px;background:linear-gradient(160deg,#f2f2f2,#b98fc6 45%,#5a4c44 75%,#efefef)" role="img" aria-label="Purple orchid beside spa stones and a towel"></div>
  <div class="abs card-title" style="left:419px">LOREM IPSUM DOLOR SIT</div>
  <p class="abs card-text" style="left:419px">Lorem ipsum dolor sit amet, consectetur adipiscing elit. Sed at ante.</p>
  <div class="abs btn card-btn" style="left:483px">READ MORE</div>

  <div class="abs card-img" style="left:604px;background:linear-gradient(135deg,#7cb648,#b5472e 50%,#6aa63c)" role="img" aria-label="Fresh salad with feta and sun-dried tomatoes"></div>
  <div class="abs card-title" style="left:604px">LOREM IPSUM DOLOR SIT</div>
  <p class="abs card-text" style="left:604px">Lorem ipsum dolor sit amet, consectetur adipiscing elit. Sed at ante.</p>
  <div class="abs btn card-btn" style="left:669px">READ MORE</div>
</section>

<footer>
  <div class="abs footer-rule"></div>
  <div class="abs footer-nav"><span>Home</span><span>Vibrelaxis</span><span>About Us</span><span>Our Services</span><span>Wellness Tips</span><span>Contact Us</span></div>
  <div class="abs footer-social" style="left:655px" role="img" aria-label="Social network link"></div>
  <div class="abs footer-social" style="left:691px" role="img" aria-label="Social network link"></div>
  <div class="abs footer-social" style="left:733px" role="img" aria-label="Social network link"></div>
  <div class="abs copyright">© Copyright 2013. All Rights Reserved.</div>
</footer>

</body>
</html>
```